Brindle Logistics Business Card Design

We are a trucking and warehousing company. We run freight in the US manly from the Pacific NW to TX and back up the the PNW. We also do warehousing where we store, move, and distribute freight. Looking for a clean and modern design of business card. We would like to look rich and elegant. Attached is our logo.

Industry/Entity Type

Trucking Company

Contact Information for Business Card

Looking for a clean and modern design of business card. We would like to look rich and elegant.

Font styles to use
Sans Serif

Colors

Designer to choose colors to be used in the design.

Requirements
Must have
• logo but it should not dominate the card
Should not have
• logo should not dominate the card

```html
<!DOCTYPE html>
<html lang="en">
<head>
<meta charset="utf-8">
<title>Brindle Logistics Business Card</title>
<link rel="stylesheet" href="https://fonts.googleapis.com/css2?family=Montserrat:wght@300;400;500;700&display=swap">
<style>
  :root {
    --backdrop: #e8e8e8;
    --card: #232323;
    --brand-blue: #0a6fc2;
    --watermark: #3b3b3b;
    --ink-light: #f2f2f2;
  }
  html, body {
    margin: 0;
    width: 1200px;
    height: 909px;
    overflow: hidden;
    background: var(--backdrop);
    font-family: "Montserrat", sans-serif;
  }
  .card {
    position: absolute;
    width: 766px;
    height: 437px;
    background: var(--card);
    overflow: hidden;
    transform-origin: top left;
    transform: scale(0.914);
    box-shadow: 0 6px 18px rgba(0,0,0,0.18);
  }
  .card--back { left: 250px; top: 30px; }
  .card--front { left: 250px; top: 472px; }

  .brand-mark {
    position: absolute;
    inset: 0;
    display: flex;
    align-items: center;
    justify-content: center;
    gap: 16px;
  }
  .brand-mark__dot {
    width: 22px; height: 22px;
    border-radius: 50%;
    background: var(--brand-blue);
  }
  .brand-mark__name {
    color: var(--brand-blue);
    font-weight: 700;
    font-size: 40px;
    letter-spacing: 1px;
  }

  .watermark {
    position: absolute;
    white-space: nowrap;
    color: var(--watermark);
    font-weight: 400;
    line-height: 1;
  }
  .watermark--top { left: -18px; top: 0; font-size: 172px; letter-spacing: 0; }
  .watermark--bottom { left: 6px; top: 182px; font-size: 92px; letter-spacing: 1px; }

  .person {
    position: absolute;
    right: 30px;
    top: 92px;
    text-align: right;
  }
  .person__name {
    color: var(--brand-blue);
    font-weight: 700;
    font-size: 42px;
    line-height: 1.05;
    letter-spacing: 0.5px;
  }
  .person__role {
    color: var(--ink-light);
    font-weight: 400;
    font-size: 25px;
    margin-top: 2px;
  }

  .contact {
    position: absolute;
    top: 282px;
    width: 260px;
    text-align: center;
    color: var(--ink-light);
    font-size: 17.5px;
    line-height: 25px;
  }
  .contact--phone { left: -23px; }
  .contact--web { left: 235px; }
  .contact--place { left: 501px; }
  .contact__icon { display: block; margin: 0 auto 14px; }
</style>
</head>
<body>
  <section class="card card--back" aria-label="Card back">
    <div class="brand-mark">
      <span class="brand-mark__dot"></span>
      <span class="brand-mark__name">Brindle Logistics</span>
    </div>
  </section>

  <section class="card card--front" aria-label="Card front">
    <div class="watermark watermark--top">BRINDLE</div>
    <div class="watermark watermark--bottom">LOGISTICS, LLC</div>

    <div class="person">
      <div class="person__name">DANIEL R. MOORE</div>
      <div class="person__role">Founder / CEO</div>
    </div>

    <div class="contact contact--phone">
      <svg class="contact__icon" width="38" height="38" viewBox="0 0 38 38">
        <circle cx="19" cy="19" r="17" fill="none" stroke="#0a6fc2" stroke-width="2.5"/>
        <path d="M14 11.5l3 0 1.3 4-2 1.4c.9 2 2.5 3.6 4.5 4.5l1.4-2 4 1.3v3c0 1-.8 1.8-1.8 1.8C17.5 25.5 12.5 20.5 12.2 13.3c0-1 .8-1.8 1.8-1.8z" fill="#0a6fc2"/>
      </svg>
      +64 (0)9555 0142<br>021 555 018
    </div>

    <div class="contact contact--web">
      <svg class="contact__icon" width="38" height="38" viewBox="0 0 38 38">
        <circle cx="19" cy="19" r="17" fill="none" stroke="#0a6fc2" stroke-width="2.5"/>
        <circle cx="19" cy="19" r="9" fill="none" stroke="#0a6fc2" stroke-width="2"/>
        <ellipse cx="19" cy="19" rx="4" ry="9" fill="none" stroke="#0a6fc2" stroke-width="1.6"/>
        <path d="M10 19h18M11.5 14.5h15M11.5 23.5h15" stroke="#0a6fc2" stroke-width="1.6"/>
      </svg>
      www.brindlelogistics.com<br>info@brindlelogistics.com
    </div>

    <div class="contact contact--place">
      <svg class="contact__icon" width="38" height="38" viewBox="0 0 38 38">
        <circle cx="19" cy="19" r="17" fill="none" stroke="#0a6fc2" stroke-width="2.5"/>
        <path d="M19 28c-4-5-6.5-8.3-6.5-11.3a6.5 6.5 0 0 1 13 0c0 3-2.5 6.3-6.5 11.3z" fill="none" stroke="#0a6fc2" stroke-width="2.2"/>
        <circle cx="19" cy="16.8" r="2.3" fill="#0a6fc2"/>
      </svg>
      48 Kestrel Lane,<br>Ferndale, Westhaven 4417,<br>Verdania
    </div>
  </section>
</body>
</html>
```